Kestrel Photography Business Card

I need a business card designed for a photography business based in Perth, Western Australia called Kestrel Photography.

We specialise in wedding, event photography and portrait photography.

The business card must borrow the style of the attached logo.

The hex codes for the colours in the logo are:
#ED1D85 - Pink
#89C23E - Green
#37282F - Black

The name on the card will be:
Name: Torvane
Phone: 0417395286
Website: www.kestrelphotography.example.au
Facebook: kestrelphotography

I am open and happy to accept creative concepts.

I’d like some space at the back for writing notes and appointment details.

```html
<!DOCTYPE html>
<html lang="en">
<head>
<meta charset="utf-8">
<title>Kestrel Photography – Business Card</title>
<link rel="stylesheet" href="https://fonts.googleapis.com/css2?family=Open+Sans:ital,wght@0,400;0,700;1,600&display=swap">
<style>
  :root {
    --pink: #ED1D85;
    --green: #A3C83E;
    --ink: #37282F;
    --back: #45383F;
    --paper: #FFFFFF;
    --rule: #B9B4B7;
    --stage: #ECECF0;
    --text: #3A3A3A;
  }
  * { box-sizing: border-box; margin: 0; padding: 0; }
  html, body {
    width: 1200px;
    height: 987px;
    overflow: hidden;
    background: var(--stage);
    font-family: "Open Sans", Arial, sans-serif;
  }
  .card {
    position: absolute;
    left: 280px;
    width: 640px;
    height: 391px;
    border-radius: 28px;
    overflow: hidden;
    box-shadow: 0 6px 22px rgba(0,0,0,0.12);
  }
  .card--front { top: 80px; background: var(--paper); }
  .card--back  { top: 516px; background: var(--back); }
  .card svg { display: block; width: 640px; height: 391px; }

  .brand-name {
    font-family: "Open Sans", Arial, sans-serif;
    font-weight: 400;
    letter-spacing: 6px;
    text-transform: uppercase;
  }
  .brand-name--front { font-size: 15px; fill: var(--text); }
  .brand-name--back  { font-size: 12px; fill: var(--paper); letter-spacing: 4px; }

  .contact { font-size: 17px; fill: var(--text); }
  .holder-name { font-size: 26px; font-weight: 700; fill: var(--pink); letter-spacing: 1px; }
  .notes-label { font-size: 17px; font-weight: 600; font-style: italic; fill: #111; }
  .back-web { font-size: 15px; fill: #D9D4D7; letter-spacing: 1.5px; }
</style>
</head>
<body>

<section class="card card--front" aria-label="Business card front">
  <svg viewBox="0 0 640 391" xmlns="http://www.w3.org/2000/svg">
    <path class="accent-green" d="M232 0 C420 40 520 250 568 391 L640 391 L640 0 Z" fill="var(--green)"/>
    <path class="accent-pink" d="M200 0 C392 38 494 250 545 391" fill="none" stroke="var(--pink)" stroke-width="10"/>

    <g class="brand-lockup">
      <circle cx="230" cy="112" r="36" fill="var(--pink)"/>
      <text class="brand-name brand-name--front" x="60" y="180">Kestrel Photography</text>
    </g>

    <g class="contact-list">
      <g class="icon-phone" transform="translate(66 250)">
        <circle r="8" fill="none" stroke="var(--green)" stroke-width="1.6"/>
        <path d="M-3 -4 q-1 5 4 8 l2 -2 l-2 -2 l-1 1 q-2 -1 -2 -3 l1 -1 l-1 -2 Z" fill="var(--green)"/>
      </g>
      <text class="contact" x="84" y="256">0417395286</text>

      <rect class="icon-social" x="58" y="274" width="16" height="16" rx="2" fill="#4A5F95"/>
      <text class="contact" x="84" y="288">kestrelphotography</text>

      <g class="icon-web" transform="translate(66 314)" fill="none" stroke="var(--green)" stroke-width="1.5">
        <circle r="8"/>
        <ellipse rx="3.5" ry="8"/>
        <line x1="-8" y1="0" x2="8" y2="0"/>
      </g>
      <text class="contact" x="84" y="320">www.kestrelphotography.example.au</text>
    </g>

    <text class="holder-name" x="612" y="222" text-anchor="end">TORVANE</text>
  </svg>
</section>

<section class="card card--back" aria-label="Business card back">
  <svg viewBox="0 0 640 391" xmlns="http://www.w3.org/2000/svg">
    <g class="notes-panel">
      <rect x="24" y="60" width="380" height="262" fill="var(--paper)"/>
      <text class="notes-label" x="40" y="88">notes:</text>
      <g stroke="var(--rule)" stroke-width="1">
        <line x1="96" y1="92" x2="388" y2="92"/>
        <line x1="40" y1="130" x2="388" y2="130"/>
        <line x1="40" y1="168" x2="388" y2="168"/>
        <line x1="40" y1="206" x2="388" y2="206"/>
        <line x1="40" y1="244" x2="388" y2="244"/>
        <line x1="40" y1="282" x2="388" y2="282"/>
      </g>
    </g>

    <g class="brand-lockup">
      <circle cx="522" cy="112" r="32" fill="var(--paper)"/>
      <text class="brand-name brand-name--back" x="522" y="180" text-anchor="middle">Kestrel Photography</text>
    </g>

    <text class="back-web" x="214" y="358" text-anchor="middle">www.kestrelphotography.example.au</text>
  </svg>
</section>

</body>
</html>
```